Simple and Approachable Cover for Pet Expo Company Page

Size: 2000 x 430; looking simply for words "Dunmore HR Consulting" and email address "DunmoreHRConsulting@brelvamail.com." This is for a cover photo for a company profile page for the Hollow Oak Expo, where I am a featured speaker on Employee Communications later this month. You can incorporate the attached photo to the left of the banner ad if you wish. The mood I wish to present is approachable, positive and simple.

Target Market(s)

small pet retail business owners

Industry/Entity Type

Pet Shop

Font styles to use
Serif
Sans Serif

Requirements
Must have
• Email address clearly defined/separated. Easy to read.
Nice to have
• I like the picture that I included; subtle pet paw background is also nice
Should not have
• No paid stock images

```html
<!DOCTYPE html>
<html lang="en">
<head>
<meta charset="utf-8">
<title>Dunmore HR Consulting – Cover Banner</title>
<link rel="stylesheet" href="https://fonts.googleapis.com/css2?family=Domine:wght@700&family=Raleway:wght@400&display=swap">
<style>
  :root {
    --page-bg: #ffffff;
    --banner-green: #a7d72a;
    --ink: #111111;
    --divider: #0d0d0d;
    --photo-sky: #9aa571;
    --photo-mid: #6e7a3e;
    --photo-grass: #8e8b4a;
  }
  html, body {
    margin: 0;
    padding: 0;
    width: 1200px;
    height: 1000px;
    overflow: hidden;
    background: var(--page-bg);
  }
  .canvas {
    position: relative;
    width: 1200px;
    height: 1000px;
  }
  .cover-banner {
    position: absolute;
    left: 32px;
    top: 378px;
    width: 1136px;
    height: 244px;
    display: block;
  }
  .banner-field { fill: var(--banner-green); }
  .banner-divider { stroke: var(--divider); stroke-width: 3; }
  .company-name {
    font-family: "Domine", Georgia, serif;
    font-weight: 700;
    font-size: 60px;
    fill: var(--ink);
  }
  .company-email {
    font-family: "Raleway", Arial, sans-serif;
    font-weight: 400;
    font-size: 31px;
    fill: var(--ink);
  }
</style>
</head>
<body>
  <main class="canvas">
    <svg class="cover-banner" viewBox="0 0 1136 244" xmlns="http://www.w3.org/2000/svg">
      <defs>
        <linearGradient id="portrait-tones" x1="0" y1="0" x2="0" y2="1">
          <stop offset="0" stop-color="var(--photo-sky)"/>
          <stop offset="0.45" stop-color="var(--photo-mid)"/>
          <stop offset="1" stop-color="var(--photo-grass)"/>
        </linearGradient>
      </defs>

      <rect class="banner-field" x="0" y="0" width="1136" height="244"/>

      <polygon class="portrait-photo" role="img"
               aria-label="Photo of a smiling couple sitting on the grass under oak trees with their two hound dogs"
               points="771,0 1136,0 1136,244 821,244"
               fill="url(#portrait-tones)"/>

      <line class="banner-divider" x1="755" y1="0" x2="806" y2="244"/>

      <text class="company-name" x="58" y="123" textLength="708" lengthAdjust="spacingAndGlyphs">Dunmore HR Consulting</text>
      <text class="company-email" x="751" y="175" text-anchor="end">DunmoreHRConsulting@brelvamail.com</text>
    </svg>
  </main>
</body>
</html>
```